Estou muito feliz om o resultado final do trabalho de vocês gostaria de agradecer a toda a equipe que me ajudou na construção desse projeto. Parabenizar em especial o MARCELO do 0800... muito solicito presta um ótimo atendimento.

```html
<!DOCTYPE html>
<html lang="pt-BR">
<head>
<meta charset="UTF-8">
<title>Cartão Fidelidade – Rafael Moura Personal Trainer</title>
<link rel="stylesheet" href="https://fonts.googleapis.com/css2?family=Open+Sans:wght@400;700;800&display=swap">
<style>
  :root {
    --page-bg: #e9e7e4;
    --card-black: #050505;
    --card-white: #ffffff;
    --brand-red: #e3141b;
    --text-white: #ffffff;
    --text-grey: #7a7a7a;
    --stamp-grey: #8c8c8c;
    --shadow: rgba(0, 0, 0, 0.18);
  }
  * { margin: 0; padding: 0; box-sizing: border-box; }
  html, body {
    width: 1200px;
    height: 1200px;
    overflow: hidden;
    background: var(--page-bg);
    font-family: "Open Sans", Arial, sans-serif;
  }
  .card {
    position: absolute;
    left: 290px;
    width: 620px;
    height: 340px;
    border-radius: 40px;
    overflow: hidden;
    box-shadow: 0 6px 18px var(--shadow);
  }
  /* Front */
  .card--front { top: 230px; background: var(--card-black); }
  .brand-dot {
    position: absolute;
    left: 394px;
    top: 48px;
    width: 48px;
    height: 48px;
    border-radius: 50%;
    background: var(--text-white);
  }
  .brand-name {
    position: absolute;
    left: 172px;
    top: 186px;
    font-weight: 800;
    font-size: 38px;
    line-height: 1;
    color: var(--text-white);
    letter-spacing: -0.5px;
  }
  .brand-role {
    position: absolute;
    left: 210px;
    top: 230px;
    font-weight: 700;
    font-size: 20px;
    line-height: 1;
    color: var(--brand-red);
  }
  .card-title {
    position: absolute;
    left: 137px;
    top: 292px;
    font-size: 28px;
    font-weight: 400;
    line-height: 1;
    color: var(--text-white);
  }
  /* Back */
  .card--back { top: 645px; background: var(--card-white); }
  .card-note {
    position: absolute;
    top: 16px;
    width: 100%;
    text-align: center;
    font-size: 12.5px;
    line-height: 19px;
    color: var(--text-grey);
  }
  .stamp-grid {
    position: absolute;
    left: 130px;
    top: 82px;
    width: 420px;
    display: grid;
    grid-template-columns: repeat(5, 1fr);
    row-gap: 56px;
    justify-items: center;
  }
  .stamp-slot {
    width: 40px;
    height: 40px;
    border-radius: 50%;
    background: var(--stamp-grey);
  }
  .card-contacts {
    position: absolute;
    top: 298px;
    left: 88px;
    display: flex;
    gap: 120px;
    font-size: 16px;
    color: var(--text-grey);
  }
  .contact { display: flex; align-items: center; gap: 8px; }
  .contact-square {
    width: 20px;
    height: 20px;
    border-radius: 3px;
    background: var(--brand-red);
  }
  .contact-icon { width: 20px; height: 20px; }
</style>
</head>
<body>
  <section class="card card--front">
    <div class="brand-dot"></div>
    <h1 class="brand-name">Rafael Moura</h1>
    <p class="brand-role">Personal Trainer</p>
    <h2 class="card-title">CARTÃO FIDELIDADE</h2>
  </section>

  <section class="card card--back">
    <p class="card-note">Lorem ipsum dolor sit amet, consectetur adipiscing elit,<br>sed do eiusmod tempor incididunt ut labore et dolore magna aliqua.</p>
    <div class="stamp-grid">
      <span class="stamp-slot"></span><span class="stamp-slot"></span><span class="stamp-slot"></span><span class="stamp-slot"></span><span class="stamp-slot"></span>
      <span class="stamp-slot"></span><span class="stamp-slot"></span><span class="stamp-slot"></span><span class="stamp-slot"></span><span class="stamp-slot"></span>
    </div>
    <div class="card-contacts">
      <span class="contact"><span class="contact-square"></span>/exemplo</span>
      <span class="contact">
        <svg class="contact-icon" viewBox="0 0 20 20" aria-hidden="true">
          <circle cx="10" cy="10" r="9" fill="#e3141b"/>
          <g fill="none" stroke="#fff" stroke-width="1.3">
            <ellipse cx="10" cy="10" rx="4" ry="8"/>
            <line x1="2" y1="10" x2="18" y2="10"/>
            <line x1="10" y1="2" x2="10" y2="18"/>
          </g>
        </svg>
        Contato@exemplo.com
      </span>
    </div>
  </section>
</body>
</html>
```